Korelith InsurTech Website Redesign - 10 Pages

Design a modern, professional website for Korelith, an AI-native cyber insurance platform serving SMBs.

DELIVERABLE: 10 pages (desktop + mobile mockups)
- Homepage (priority #1)
- 4 Platform pages (Cyber Insurance, Brokers, Underwriters, Policyholder)
- 3 Company pages (About Us, Team, Contact/Careers)
- 2 Risk pages (AI Risk, Cyber Risk)

DESIGN DIRECTION:
- Professional + innovative (insurance meets technology)
- Trust-building + modern aesthetic
- Reference: Brambury Insurance, Tidewick Insurance
- Use official brand colors (6-color palette provided)
- Avoid generic security clipart (padlocks, shields, magnifying glasses)
- Custom graphics, not AI-generated or stock imagery

CURRENT SITES FOR REFERENCE:
- www.korelith.ai
- https://a3c9124d.korelith-website.vorlapages.dev/

Full detailed brief with all content, page specifications, and brand guidelines attached as PDF (Korelith_PixelHarbor_Brief.pdf).

TARGET AUDIENCE: Insurance brokers (primary), SMB business owners (secondary)
KEY MESSAGE: "Cyber Insurance the Way It Should Be"

Additional brand assets available in Google Drive - link provided on request.

```html
<!DOCTYPE html>
<html lang="en">
<head>
<meta charset="UTF-8">
<title>Korelith — About Us</title>
<link href="https://fonts.googleapis.com/css2?family=Arimo:wght@400;600;700&display=swap" rel="stylesheet">
<style>
  :root {
    --navy: #152142;
    --navy-deep: #17244a;
    --navy-soft: #1d2d58;
    --teal: #6ad1c9;
    --teal-dark: #0e8aa0;
    --teal-deep: #0b7a90;
    --paper: #f4f5fa;
    --card: #ffffff;
    --ink: #0f1629;
    --white: #ffffff;
  }
  * { box-sizing: border-box; margin: 0; padding: 0; }
  html, body {
    width: 1200px;
    height: 882px;
    overflow: hidden;
  }
  body {
    font-family: "Arimo", Arial, sans-serif;
    background: var(--paper);
    color: var(--ink);
    position: relative;
  }

  .site-header {
    position: absolute;
    top: 0; left: 0; right: 0;
    height: 30px;
    z-index: 2;
  }
  .brand {
    position: absolute;
    left: 50px; top: 1px;
    font-size: 21px;
    font-weight: 700;
    color: var(--white);
  }
  .main-nav {
    position: absolute;
    left: 658px; top: 6px;
    font-size: 14px;
    color: var(--white);
  }
  .main-nav span { position: absolute; white-space: nowrap; }
  .main-nav .has-menu::after {
    content: "";
    display: inline-block;
    margin-left: 7px;
    vertical-align: middle;
    border-left: 3px solid transparent;
    border-right: 3px solid transparent;
    border-top: 4px solid var(--white);
  }
  .btn {
    display: flex;
    align-items: center;
    justify-content: center;
    background: var(--teal);
    color: var(--white);
    font-size: 14px;
    border-radius: 0 0 4px 4px;
  }
  .btn-demo {
    position: absolute;
    left: 1010px; top: 0;
    width: 123px; height: 30px;
  }

  .hero {
    position: absolute;
    top: 0; left: 0;
    width: 1200px; height: 406px;
    background: var(--navy);
    border-bottom: 1px solid #0b1226;
  }
  .hero-copy {
    position: absolute;
    left: 50px; width: 685px;
    top: 186px;
    text-align: center;
    color: var(--white);
  }
  .hero-copy h1 { font-size: 36px; font-weight: 700; line-height: 1.1; }
  .hero-copy p { margin-top: 24px; font-size: 14.5px; }
  .hero-visual {
    position: absolute;
    left: 772px; top: 100px;
    width: 360px; height: 251px;
    border-radius: 11px;
    background: linear-gradient(135deg, var(--teal-dark), var(--teal-deep));
  }

  .about {
    position: absolute;
    top: 406px; left: 0;
    width: 1200px; height: 315px;
    background: var(--paper);
  }
  .mission {
    position: absolute;
    left: 50px; top: 58px;
  }
  .mission h2 { font-size: 22.5px; font-weight: 600; }
  .mission p { margin-top: 8px; font-size: 14px; }
  .team-title {
    position: absolute;
    left: 50px; top: 172px;
    font-size: 29px;
    font-weight: 600;
  }
  .team-card {
    position: absolute;
    top: 249px;
    width: 343px; height: 80px;
    background: var(--card);
    border-radius: 6px;
    box-shadow: 0 2px 8px rgba(15, 22, 41, 0.06);
    text-align: center;
    padding-top: 25px;
    font-size: 14.5px;
  }

  .careers {
    position: absolute;
    top: 721px; left: 0;
    width: 1200px; height: 161px;
    background: linear-gradient(180deg, var(--navy-deep), var(--navy-soft));
    border-top: 1px solid #0b1226;
    text-align: center;
    color: var(--white);
  }
  .careers h2 {
    margin-top: 78px;
    font-size: 29px;
    font-weight: 700;
    line-height: 1.1;
    text-shadow: 0 2px 4px rgba(0,0,0,0.35);
  }
  .btn-careers {
    position: absolute;
    left: 539px; top: 130px;
    width: 122px; height: 40px;
    border-radius: 4px;
    color: var(--ink);
    font-weight: 600;
    padding-bottom: 6px;
  }
</style>
</head>
<body>
  <section class="hero">
    <div class="hero-copy">
      <h1>About Us</h1>
      <p>Building trust through AI-powered insurance innovation.</p>
    </div>
    <div class="hero-visual" role="img" aria-label="Hero brand artwork placeholder"></div>
  </section>

  <header class="site-header">
    <div class="brand">Korelith</div>
    <nav class="main-nav">
      <span class="has-menu" style="left:0">Platform</span>
      <span style="left:87px">Cyber Risk</span>
      <span style="left:175px">AI Risk</span>
      <span class="has-menu" style="left:239px">Company</span>
    </nav>
    <a class="btn btn-demo">Request Demo</a>
  </header>

  <main class="about">
    <div class="mission">
      <h2>Our Mission</h2>
      <p>To modernize insurance through intelligent automation, empowering businesses with faster, smarter risk protection.</p>
    </div>
    <h2 class="team-title">Leadership Team</h2>
    <div class="team-card" style="left:50px">CEO</div>
    <div class="team-card" style="left:420px">CTO</div>
    <div class="team-card" style="left:790px">Head of Risk</div>
  </main>

  <section class="careers">
    <h2>Join Our Journey</h2>
    <a class="btn btn-careers">View Careers</a>
  </section>
</body>
</html>
```